Business Card Design

We are a family run drainage & groundworks company that specialise in treatment plant installation. We work for commercial & domestic property's, we have specialised knowledge & equipment for CCTV surveys, jetting blockages & repairing all types of drainage systems.

Industry/Entity Type

Business

Contact Information for Business Card

14 Marlpit Workshops
Belcombe Mill Lane
Harrowbridge
Wendshire
SP4 7TN
Tel: 01632 960418
Fax: 01632 960752
Mobile: 07700 900318
enquiries@kestrelwd.co.uk
www.kestrelwastedrainage.co.uk

Requirements
Must have
• logo, address, the right colour green.
I need the cards to also have individuals names:

Tom lydgate
Neil Carrow
Helen Lydgate
Di Pemberton

And also some with just the name & address on :)

```html
<!DOCTYPE html>
<html lang="en">
<head>
<meta charset="utf-8">
<title>Tom Lydgate – Business Card</title>
<link rel="stylesheet" href="https://fonts.googleapis.com/css2?family=Source+Sans+3:wght@400;700&display=swap">
<style>
  :root {
    --card-bg: #ffffff;
    --ink: #231f20;
    --brand-green: #1e9a3c;
    --edge: #dcdcdc;
  }
  html, body {
    margin: 0;
    padding: 0;
    overflow: hidden;
    background: var(--card-bg);
  }
  .card {
    position: relative;
    width: 1200px;
    height: 773px;
    box-sizing: border-box;
    border: 2px solid var(--edge);
    background: var(--card-bg);
    font-family: "Source Sans 3", "Helvetica Neue", Arial, sans-serif;
    color: var(--ink);
    overflow: hidden;
  }
  .holder-name {
    position: absolute;
    left: 78px;
    top: 66px;
    margin: 0;
    font-size: 51px;
    font-weight: 700;
    letter-spacing: -0.5px;
    line-height: 1;
  }
  .contact-list {
    position: absolute;
    left: 78px;
    top: 214px;
    margin: 0;
    padding: 0;
    list-style: none;
  }
  .contact-item {
    display: flex;
    align-items: center;
    height: 50px;
    font-size: 30px;
    line-height: 1;
  }
  .contact-label {
    width: 30px;
    font-size: 19px;
    color: var(--ink);
  }
  .contact-bullet {
    width: 8px;
    height: 8px;
    border-radius: 50%;
    background: var(--brand-green);
    margin: 0 22px 0 10px;
  }
  .postal-address {
    position: absolute;
    left: 72px;
    top: 520px;
    margin: 0;
    font-style: normal;
    font-size: 30px;
    line-height: 41px;
  }
  .website {
    position: absolute;
    left: 72px;
    top: 672px;
    margin: 0;
    font-size: 30px;
  }
  .brand {
    position: absolute;
    left: 884px;
    top: 470px;
    width: 250px;
    display: flex;
    flex-direction: column;
    align-items: center;
  }
  .brand-square {
    display: block;
    width: 172px;
    height: 172px;
  }
  .brand-name {
    margin: 12px 0 0;
    text-align: center;
    font-size: 22px;
    font-weight: 400;
    letter-spacing: 3px;
    line-height: 29px;
    text-transform: uppercase;
    color: var(--ink);
  }
</style>
</head>
<body>
  <main class="card">
    <h1 class="holder-name">Tom Lydgate</h1>

    <ul class="contact-list">
      <li class="contact-item"><span class="contact-label">T</span><span class="contact-bullet"></span>01632 960418</li>
      <li class="contact-item"><span class="contact-label">F</span><span class="contact-bullet"></span>01632 960752</li>
      <li class="contact-item"><span class="contact-label">M</span><span class="contact-bullet"></span>07700 900318</li>
      <li class="contact-item"><span class="contact-label">E</span><span class="contact-bullet"></span>enquiries@kestrelwd.co.uk</li>
    </ul>

    <address class="postal-address">
      14 Marlpit Workshops<br>
      Belcombe Mill Lane Harrowbridge<br>
      Wendshire SP4 7TN
    </address>

    <p class="website">www.kestrelwastedrainage.co.uk</p>

    <div class="brand">
      <svg class="brand-square" viewBox="0 0 172 172" aria-hidden="true">
        <rect width="172" height="172" fill="var(--brand-green)"/>
      </svg>
      <p class="brand-name">Kestrel Waste<br>&amp; Drainage</p>
    </div>
  </main>
</body>
</html>
```